Larkspur Ridge Management - Business Cards

I need business cards. My current logo was designed by a designer at this site and I very much like and am happy with the results. I would like a business card that is trendy, unique, current yet professional. I deal with high net worth clients daily

Target Market(s)

Out of state investors looking to get into the rental market in Ohio

Industry/Entity Type

Property Management, Consulting

Contact Information for Business Card

Name, Title (Chief Financial Officer) office phone number (555) 817-3094 website address larkridgemgmt.example

Font styles to use
Sans Serif

Colors
0054AA
0677BA
7BADD7
CADEEF
E8F1F8
0094D4
00A9DD
6FCCEA
C7EBF8
E9F6FB
00AB8E
00BBA5
67D7C9
C6EFE9
E9F9F6

```html
<!DOCTYPE html>
<html lang="en">
<head>
<meta charset="utf-8">
<title>Larkspur Ridge Management – Business Cards</title>
<link rel="stylesheet" href="https://fonts.googleapis.com/css2?family=Montserrat:wght@400;500;700;800&display=swap">
<style>
  :root {
    --backdrop: #cadeef;
    --card-blue: #0054aa;
    --accent-teal: #00bba5;
    --accent-teal-dark: #00ab8e;
    --accent-teal-light: #67d7c9;
    --ink-light: #ffffff;
    --ink-soft: #c7ebf8;
    --card-shadow: rgba(0, 40, 90, 0.3);
  }
  * { box-sizing: border-box; margin: 0; padding: 0; }
  html, body { width: 1200px; height: 1038px; overflow: hidden; }
  body {
    background: var(--backdrop);
    font-family: "Montserrat", sans-serif;
    color: var(--ink-light);
    position: relative;
  }
  .card {
    position: absolute;
    width: 620px;
    height: 354px;
    background: var(--card-blue);
    box-shadow: 0 10px 24px var(--card-shadow);
    overflow: hidden;
  }
  .card--front { left: 150px; top: 110px; }
  .card--back { left: 430px; top: 574px; }

  .wordmark {
    display: flex;
    align-items: center;
    gap: 12px;
  }
  .wordmark__square {
    width: 22px; height: 22px;
    background: var(--accent-teal);
    flex: none;
  }
  .wordmark__name {
    font-weight: 800;
    text-transform: uppercase;
    line-height: 1.1;
    letter-spacing: 0.02em;
  }
  .card--front .wordmark {
    position: absolute;
    left: 50%; top: 50%;
    transform: translate(-50%, -50%);
  }
  .card--front .wordmark__name { font-size: 30px; width: 300px; }

  .card--back .wordmark {
    position: absolute;
    left: 52px; top: 104px;
    gap: 10px;
  }
  .card--back .wordmark__square { width: 14px; height: 14px; }
  .card--back .wordmark__name { font-size: 17px; width: 170px; }

  .holder {
    position: absolute;
    left: 52px; top: 222px;
  }
  .holder__name { font-size: 28px; font-weight: 700; }
  .holder__title {
    font-size: 9px; font-weight: 500;
    letter-spacing: 0.12em;
    text-transform: uppercase;
    color: var(--ink-soft);
    text-align: right;
    margin-top: 2px;
  }

  .contact-list {
    position: absolute;
    left: 316px; top: 102px;
    list-style: none;
    display: flex; flex-direction: column; gap: 16px;
  }
  .contact-list__item {
    display: flex; align-items: center; gap: 12px;
    font-size: 14px; font-weight: 500;
  }
  .contact-list__item--address { font-size: 12px; line-height: 1.35; }
  .contact-list__icon { width: 20px; height: 20px; flex: none; }

  .edge-bar {
    position: absolute;
    width: 26px; height: 98px;
    background: linear-gradient(90deg, var(--accent-teal-dark), var(--accent-teal) 55%, var(--accent-teal-light));
  }
  .edge-bar--top { right: 0; top: 0; }
  .edge-bar--bottom { left: 0; bottom: 0; }
</style>
</head>
<body>
  <section class="card card--front" aria-label="Business card front">
    <div class="wordmark">
      <span class="wordmark__square"></span>
      <span class="wordmark__name">Larkspur Ridge Management</span>
    </div>
  </section>

  <section class="card card--back" aria-label="Business card back">
    <span class="edge-bar edge-bar--top"></span>
    <span class="edge-bar edge-bar--bottom"></span>

    <div class="wordmark">
      <span class="wordmark__square"></span>
      <span class="wordmark__name">Larkspur Ridge Management</span>
    </div>

    <div class="holder">
      <p class="holder__name">Daniel Weber</p>
      <p class="holder__title">Chief Financial Officer</p>
    </div>

    <ul class="contact-list">
      <li class="contact-list__item">
        <svg class="contact-list__icon" viewBox="0 0 20 20" fill="none" stroke="#fff" stroke-width="1.4">
          <circle cx="10" cy="10" r="9"/>
          <path d="M7 5.5l1.6 2-1 1.2c.6 1.4 1.6 2.4 3 3l1.2-1 2 1.6-1 1.6c-3.2-.2-6.2-3.2-6.4-6.4z" fill="#fff" stroke="none"/>
        </svg>
        <span>(555) 817-3094</span>
      </li>
      <li class="contact-list__item">
        <svg class="contact-list__icon" viewBox="0 0 20 20" fill="none" stroke="#fff" stroke-width="1.4">
          <circle cx="10" cy="10" r="9"/>
          <rect x="5.5" y="7" width="9" height="6.5" rx="0.6"/>
          <path d="M5.5 7.3l4.5 3.4 4.5-3.4"/>
        </svg>
        <span>office@larkridgemgmt.example</span>
      </li>
      <li class="contact-list__item">
        <svg class="contact-list__icon" viewBox="0 0 20 20" fill="none" stroke="#fff" stroke-width="1.4">
          <circle cx="10" cy="10" r="9"/>
          <circle cx="10" cy="10" r="4.5"/>
          <path d="M5.5 10h9M10 5.5c-1.8 2.6-1.8 6.4 0 9M10 5.5c1.8 2.6 1.8 6.4 0 9"/>
        </svg>
        <span>www.larkridgemgmt.example</span>
      </li>
      <li class="contact-list__item contact-list__item--address">
        <svg class="contact-list__icon" viewBox="0 0 20 20" fill="none" stroke="#fff" stroke-width="1.4">
          <circle cx="10" cy="10" r="9"/>
          <path d="M10 15s-3.5-3.6-3.5-6.2a3.5 3.5 0 017 0C13.5 11.4 10 15 10 15z"/>
          <circle cx="10" cy="8.8" r="1.2" fill="#fff" stroke="none"/>
        </svg>
        <span>Suite 204, 4410 Meadow Ln,<br>Columbus, OH 43201</span>
      </li>
    </ul>
  </section>
</body>
</html>
```